New Print Material Needed for Renovation Company

We are looking to update our current Print Material to reflect the current process we offer to our clients. A lot of the information is also outdated along with many of the photos that are currently being used. We are a renovation company that specializes in residential and commercial renovations and custom builds.This project is MULTIPLE pages. We will pay the chosen designer an extra fee for the designing 3-4 additional pages that are similar to the chosen design. Attached is our current Print Material. We are hoping to update the look of them and some of the messaging. Our current company colors are white, blue and light grey and it will remain that way.

Industry/Entity Type

Construction Company

Font styles to use
Sans Serif

Colors
3176b5
ffffff

Requirements
Must have
• Easy to explain the process
• Easy to read and understand let alone
• Easy to navigate
Nice to have
• As much creativity as possible
Should not have
• no confusing text
• no confusing layout

```html
<!DOCTYPE html>
<html lang="en">
<head>
<meta charset="utf-8">
<title>Our Services</title>
<link rel="stylesheet" href="https://fonts.googleapis.com/css2?family=Roboto:wght@400;500;700&display=swap">
<style>
  :root {
    --brand-blue: #1b58a3;
    --ink: #111111;
    --paper: #ffffff;
  }
  * { margin: 0; padding: 0; box-sizing: border-box; }
  html, body { width: 848px; height: 1200px; overflow: hidden; background: var(--paper); }
  .page {
    position: relative; width: 848px; height: 1200px; overflow: hidden;
    background: var(--paper); font-family: "Roboto", Arial, sans-serif; color: var(--ink);
  }
  .page-title {
    position: absolute; top: 39px; left: 0; width: 838px; text-align: center;
    font-size: 50px; line-height: 58px; font-weight: 700; color: var(--brand-blue); letter-spacing: 0.5px;
  }
  .photo-collage { position: absolute; left: 0; top: 0; }
  .service-icon {
    position: absolute; width: 90px; height: 90px; transform: translate(-50%, -50%);
  }
  .service-label {
    position: absolute; transform: translate(-50%, -50%);
    font-size: 22px; line-height: 26px; font-weight: 700;
    color: var(--brand-blue); white-space: nowrap;
  }
  .divider {
    position: absolute; left: 594px; top: 594px; width: 172px; height: 5px; background: var(--brand-blue);
  }
  .feature { position: absolute; right: 62px; text-align: right; }
  .feature-title {
    font-size: 32px; font-weight: 700; color: var(--brand-blue); line-height: 35px; letter-spacing: 0.2px;
    white-space: nowrap;
  }
  .feature-text { font-size: 17px; font-weight: 500; line-height: 20.7px; margin-top: 2px; white-space: nowrap; }
  .footer-band { position: absolute; left: 0; bottom: 0; width: 848px; height: 41px; background: var(--brand-blue); }
</style>
</head>
<body>
<div class="page">
  <h1 class="page-title">OUR SERVISES</h1>

  <svg class="photo-collage" width="848" height="1200" viewBox="0 0 848 1200">
    <defs>
      <linearGradient id="roomTones" x1="0" y1="0" x2="1" y2="1">
        <stop offset="0" stop-color="#6b5a4e"/>
        <stop offset="0.5" stop-color="#c8c2b8"/>
        <stop offset="1" stop-color="#8a4a42"/>
      </linearGradient>
      <linearGradient id="kitchenTones" x1="0" y1="0" x2="0" y2="1">
        <stop offset="0" stop-color="#eef0ee"/>
        <stop offset="0.3" stop-color="#c9d2d0"/>
        <stop offset="0.55" stop-color="#7d6f66"/>
        <stop offset="0.75" stop-color="#e6e4e0"/>
        <stop offset="1" stop-color="#b9b3ac"/>
      </linearGradient>
    </defs>
    <path role="img" aria-label="Photo of a living room with bookshelves and a telescope"
          d="M-150 353 L-10 213 L127 345 Q133 353 127 361 L-10 498 Z" fill="url(#roomTones)"/>
    <path role="img" aria-label="Photo of a bright kitchen with pendant lights, window and island"
          d="M-90 666 L190 386 Q197 379 204 386 L477 659 Q483 666 477 673 L204 948 Q197 955 190 948 Z"
          fill="url(#kitchenTones)"/>
  </svg>

  <!-- Row 1 -->
  <div class="service">
    <svg class="service-icon" style="left:175px;top:178px" viewBox="0 0 90 90"><circle cx="45" cy="45" r="45" fill="var(--brand-blue)"/>
      <g fill="none" stroke="#fff" stroke-width="5" stroke-linecap="round"><path d="M27 44V27q0-6 6-6h5"/></g>
      <path d="M22 44h47q0 14-12 16H34q-12-2-12-16z" fill="#fff"/><path d="M31 60l-3 6M59 60l3 6" stroke="#fff" stroke-width="4" stroke-linecap="round"/></svg>
    <span class="service-label" style="left:175px;top:247px">Bathrooms</span>
  </div>
  <div class="service">
    <svg class="service-icon" style="left:308px;top:178px" viewBox="0 0 90 90"><circle cx="45" cy="45" r="45" fill="var(--brand-blue)"/>
      <rect x="21" y="24" width="48" height="40" rx="4" fill="#fff"/><rect x="27" y="36" width="36" height="22" rx="2" fill="var(--brand-blue)"/>
      <circle cx="61" cy="30" r="3" fill="var(--brand-blue)"/></svg>
    <span class="service-label" style="left:306px;top:247px">Kitchens</span>
  </div>
  <div class="service">
    <svg class="service-icon" style="left:441px;top:178px" viewBox="0 0 90 90"><circle cx="45" cy="45" r="45" fill="var(--brand-blue)"/>
      <path d="M18 38 L45 24 L72 38" fill="none" stroke="#fff" stroke-width="6" stroke-linecap="round" stroke-linejoin="round"/>
      <g fill="#fff"><rect x="33" y="42" width="10" height="10" rx="2"/><rect x="47" y="42" width="10" height="10" rx="2"/><rect x="33" y="56" width="10" height="10" rx="2"/><rect x="47" y="56" width="10" height="10" rx="2"/></g></svg>
    <span class="service-label" style="left:442px;top:247px">Attics</span>
  </div>
  <div class="service">
    <svg class="service-icon" style="left:573px;top:178px" viewBox="0 0 90 90"><circle cx="45" cy="45" r="45" fill="var(--brand-blue)"/>
      <path d="M48 22 L66 20 V64 L48 70 Z" fill="#fff"/><circle cx="53" cy="46" r="2.5" fill="var(--brand-blue)"/>
      <path d="M22 40h8v-6h10v24h-6v-6h-12z" fill="#fff"/></svg>
    <span class="service-label" style="left:573px;top:247px">Basements</span>
  </div>
  <div class="service">
    <svg class="service-icon" style="left:706px;top:178px" viewBox="0 0 90 90"><circle cx="45" cy="45" r="45" fill="var(--brand-blue)"/>
      <g stroke="#fff" stroke-width="4" stroke-linecap="round"><path d="M30 50L27 22M35 50L38 22M40 50L48 25M45 50L57 31M50 51L64 40"/></g>
      <rect x="22" y="52" width="46" height="14" rx="3" fill="#fff"/></svg>
    <span class="service-label" style="left:716px;top:248px">Design</span>
  </div>

  <!-- Row 2 -->
  <div class="service">
    <svg class="service-icon" style="left:401px;top:311px" viewBox="0 0 90 90"><circle cx="45" cy="45" r="45" fill="var(--brand-blue)"/>
      <path d="M45 24V66M24 45H66" stroke="#fff" stroke-width="9" stroke-linecap="round"/></svg>
    <span class="service-label" style="left:403px;top:381px">Additions</span>
  </div>
  <div class="service">
    <svg class="service-icon" style="left:573px;top:311px" viewBox="0 0 90 90"><circle cx="45" cy="45" r="45" fill="var(--brand-blue)"/>
      <path d="M28 26 L62 62" stroke="#fff" stroke-width="7" stroke-linecap="round"/>
      <circle cx="28" cy="26" r="8" fill="#fff"/><circle cx="24" cy="22" r="4" fill="var(--brand-blue)"/>
      <path d="M64 22 L30 62" stroke="#fff" stroke-width="5" stroke-linecap="round"/>
      <path d="M54 38 L46 30 L62 18 L68 24 Z" fill="#fff"/></svg>
    <span class="service-label" style="left:545px;top:381px">Major Repair</span>
  </div>
  <div class="service">
    <svg class="service-icon" style="left:706px;top:314px" viewBox="0 0 90 90"><circle cx="45" cy="45" r="45" fill="var(--brand-blue)"/>
      <g fill="none" stroke="#fff" stroke-width="4" stroke-linecap="round"><path d="M30 22h-6v46h42V22H52M38 22h6v10M24 46h18M50 46h16M44 54v14"/></g></svg>
    <span class="service-label" style="left:699px;top:380px">Custom Home</span>
  </div>

  <!-- Row 3 -->
  <div class="service">
    <svg class="service-icon" style="left:706px;top:455px" viewBox="0 0 90 90"><circle cx="45" cy="45" r="45" fill="var(--brand-blue)"/>
      <g fill="none" stroke="#fff" stroke-width="4"><circle cx="45" cy="33" r="6"/><path d="M34 59v-5q0-6 6-6h10q6 0 6 6v5z"/>
      <circle cx="27" cy="38" r="4"/><path d="M25 58h-4v-6q0-3 3-3"/>
      <circle cx="63" cy="38" r="4"/><path d="M65 58h4v-6q0-3-3-3"/></g></svg>
    <span class="service-label" style="left:706px;top:521px">In Law Suite</span>
  </div>

  <div class="divider"></div>

  <section class="feature" style="top:664px">
    <h2 class="feature-title">ONE-STOP SHOP</h2>
    <p class="feature-text">We don't do any out-of-the-box<br>renovations. Each project starts<br>with us learning about your needs.<br>Our design and build services include<br>3D renders and floor plans before the<br>actual renovation, so you can visually see<br>what you're getting before you even commit.</p>
  </section>

  <section class="feature" style="top:864px">
    <h2 class="feature-title">EXPERTS AT EVERY STEP</h2>
    <p class="feature-text">Our full-service approach means that you don't have to<br>worry about finding a designer, an electrician or a painter -<br>we've got it covered, and our team of skilled professionals will<br>be with you every step of the way, from the first sketch to the last<br>coat of paint.</p>
  </section>

  <section class="feature" style="top:1023px">
    <h2 class="feature-title">STUNNING RENOVATIONS</h2>
    <p class="feature-text">With more than 50 years of combined experience, our network of local<br>suppliers allows us to create luxurious renovations at very affordable prices.</p>
  </section>

  <div class="footer-band"></div>
</div>
</body>
</html>
```